Volunteer Marketplace Needs New Look - www.Mipsko.org

Mipsko is the first online marketplace that lets you buy or sell volunteered services to raise money for charity. (www.Mipsko.org)

We went into live testing a few months ago to get some feedback and feel we need to redo the design. Some points:

- The current design was developed when a previous logo was being used. We later developed the current logo (which we love) and have never felt it really fit into the design. A design that plays up the logo would be great but not required.

- The circles in the logo represent coins which is a theme we are using in our branding (our business cards are coins). The marketplace offers a new form of currency people can use to give back. We don't feel the design should center around this concept, but a small element would be a nice touch.

We want a design that is engaging and fun - but still professional and credible.
Updates

I just want to thank you all for submitting designs. I have been trying to send feedback to everyone and am starting to eliminate designs so I can begin to narrow it. It is so hard to decide. You all did a great job! 

Target Market(s)

There are three target audiences - volunteers donating their services, customers buying donated services, and charities joining the program.

Industry/Entity Type

Business

Requirements
Must have
• - We feel we need to represent on the home page the concept of there being two parties that are coming together - the Volunteer and the Customer.

- We have a 60 second overview video in the works that we would like displayed on the home page.
Nice to have
• Incase it is helpful, here are some designs we like - but please know we are looking for creative ideas. Your design does not have to look like these.

http://www.lendora-sample.org/
https://www.wexaro.com/
http://www.layoutbarn.com/website-templates/40056.html
http://www.layoutbarn.com/website-templates/40121.html
http://www.pixelhive.com/

Also - please be creative about what content we put on our home page. We want to modernize the site. We can feed in our blog, twitter, facebook, etc into the home page if you think we should. We need your expertise to recommend what we need to showcase.
Should not have
• Please note that the paragraphs of content do not have to be on the home page. These are there now, but feedback tells us it is too boring - and they is why we are having the video done. So - you do not have to make room for all that text.

```html
<!DOCTYPE html>
<html lang="en">
<head>
<meta charset="utf-8">
<title>Mipsko – The new way to give</title>
<link rel="stylesheet" href="https://fonts.googleapis.com/css2?family=Open+Sans:wght@400;600;700&display=swap">
<style>
:root{
  --blue:#2a6d9e;--blue-dark:#17507a;--blue-deep:#123f63;--teal:#1f6a93;
  --lime:#b6e03a;--lime-dark:#8cbf1c;--ink:#333;--grey:#666;--light:#eeeeee;
  --panel-head:#3d4850;--white:#fff;--logo:#3f8fb0;
}
*{box-sizing:border-box;margin:0;padding:0}
html,body{width:949px;height:1200px;overflow:hidden}
body{position:relative;background:var(--light);font-family:Arial,Helvetica,sans-serif;color:var(--ink);font-size:11px}
.abs{position:absolute}
.open{font-family:'Open Sans',Arial,sans-serif}
/* header */
.site-header{left:0;top:0;width:949px;height:93px;background:linear-gradient(#fafafa,#ececec)}
.brand{left:104px;top:12px}
.brand-name{font-family:'Open Sans',sans-serif;font-weight:700;font-size:42px;color:var(--logo);letter-spacing:1px;line-height:50px}
.brand-tag{font-family:'Open Sans',sans-serif;font-size:12px;color:var(--grey);margin-left:44px;margin-top:-4px}
.social{top:19px;display:flex;gap:3px}
.social span{width:13px;height:13px;border-radius:50%;display:block}
.auth{left:586px;top:20px;font-size:10px;color:#444}
.search{left:676px;top:14px;width:170px;height:23px;border:1px solid #ccc;border-radius:3px;background:#fff;font-size:10px;color:#999;padding:5px 7px}
.nav{top:50px;height:24px;color:#fff;font-family:'Open Sans',sans-serif;font-size:11px;text-align:center;line-height:24px;border-radius:2px;background:linear-gradient(#5a5f63,#3c4145)}
.nav.active{background:linear-gradient(#2f82b3,#1b618e)}
/* hero */
.hero{left:0;top:93px;width:949px;height:315px;background:radial-gradient(circle at 30% 40%,#3b8cc0,#1f5e8c 70%)}
.hero h1{left:100px;top:145px;font-family:'Open Sans',sans-serif;font-weight:700;font-size:35px;color:#fff}
.hero-lede{left:102px;top:190px;width:380px;font-size:10.5px;line-height:13px;color:#fff}
.action{width:98px;height:98px;border-radius:50%;background:radial-gradient(circle at 40% 35%,#d4f26a,var(--lime-dark));top:229px;display:flex;align-items:center;justify-content:center}
.action-label{top:335px;width:140px;text-align:center;font-family:'Open Sans',sans-serif;font-size:14px;font-weight:600;color:#fff;line-height:18px}
.community{left:546px;top:100px;width:300px;height:300px;border-radius:50%;border:3px solid #fff;background:linear-gradient(135deg,#8a6e58,#3b3f44 50%,#a98b6f)}
.bubble{border-radius:50%;border:2px solid #fff;background:#2a2e33}
/* intro */
.video{left:108px;top:444px;width:144px;height:144px;border-radius:50%;border:4px solid #fff;background:linear-gradient(135deg,#b89a7c,#5a4030);box-shadow:0 0 3px rgba(0,0,0,.3)}
.play{left:162px;top:502px;width:36px;height:36px;border-radius:50%;background:var(--blue-deep);border:2px solid #fff}
.video-cap{left:145px;top:566px;font-size:8px;color:#fff}
.video-shadow{left:130px;top:600px;width:100px;height:12px;border-radius:50%;background:radial-gradient(rgba(0,0,0,.25),transparent 70%)}
.intro-head{left:275px;top:453px;font-family:'Open Sans',sans-serif;font-size:11.5px;font-weight:600;color:var(--teal);line-height:16px}
.intro-text{left:275px;width:335px;font-size:9.5px;line-height:13.5px;color:var(--grey)}
.share{top:596px;height:15px;border:1px solid #ccc;background:#f6f6f6;font-size:8px;line-height:13px;padding:0 4px;color:#345}
.charity{left:660px;top:442px;width:186px;height:175px;background:#fff;box-shadow:0 0 2px rgba(0,0,0,.25)}
.box-head{height:30px;background:linear-gradient(#56606a,#38424a);color:#fff;font-family:'Open Sans',sans-serif;font-size:12.5px;line-height:30px;padding-left:12px}
.charity-name{display:flex;align-items:center;gap:8px;padding:28px 0 0 16px;font-family:'Open Sans',sans-serif;font-size:20px;color:#1d5e3a}
.charity-name i{width:48px;height:48px;border-radius:50%;background:#1d5e3a;display:block}
.dots{position:absolute;left:72px;top:158px;display:flex;gap:3px}
.dots span{width:7px;height:7px;border-radius:50%;background:#888}
.dots span:first-child{background:var(--teal)}
/* banner */
.banner{left:103px;top:651px;width:743px;height:56px;background:linear-gradient(#e6e6e6,#cfcfcf);border-radius:3px;box-shadow:0 2px 3px rgba(0,0,0,.2)}
.banner h3{position:absolute;left:19px;top:10px;font-family:'Open Sans',sans-serif;font-size:12px;color:var(--teal)}
.banner p{position:absolute;left:19px;top:28px;font-size:9.5px;color:#444}
.cta{position:absolute;left:366px;top:4px;width:196px;height:42px;border-radius:3px;background:linear-gradient(#c9ee52,var(--lime-dark));font-family:'Open Sans',sans-serif;font-weight:700;font-size:15px;color:#2a3a10;text-align:center;line-height:42px}
.banner-mark{position:absolute;left:618px;top:0;width:125px;height:52px;background:#5b5f62;border-radius:0 3px 3px 0;font-family:'Open Sans',sans-serif;font-size:22px;color:#7f8487;padding:6px 0 0 22px}
/* listings */
.panel{top:733px;width:348px;height:256px;background:#fff;box-shadow:0 0 2px rgba(0,0,0,.3)}
.panel .box-head{height:32px;line-height:32px}
.view-all{position:absolute;right:20px;top:7px;height:17px;padding:0 9px;background:#5a646b;border:1px solid #7a848b;font-size:8.5px;line-height:15px;color:#fff}
.item{position:absolute;left:12px;width:322px;height:95px}
.item+.item{border-top:1px solid #e5e5e5}
.photo{position:absolute;left:0;width:93px;height:86px;border:3px solid #fff;box-shadow:0 0 2px rgba(0,0,0,.4)}
.item h4{position:absolute;left:104px;top:0;font-family:'Open Sans',sans-serif;font-weight:400;font-size:11.5px;color:var(--teal)}
.item .meta{position:absolute;left:104px;top:17px;font-size:9px;color:#222}
.item .desc{position:absolute;left:104px;top:29px;width:215px;font-size:9px;line-height:11.5px;color:#555}
.item .more{position:absolute;left:104px;top:70px;height:15px;padding:0 6px;background:var(--teal);color:#fff;font-size:9px;line-height:15px;border-radius:2px}
.item .stat{position:absolute;left:161px;top:73px;font-size:8px;color:#777}
/* footer */
.site-footer{left:0;top:1030px;width:949px;height:140px;background:linear-gradient(#2568a0,#1b5886);border-top:1px solid #174a72}
.foot-brand{left:110px;top:1060px;font-family:'Open Sans',sans-serif;font-weight:700;font-size:34px;color:#6e9fc2}
.foot-tag{left:146px;top:1104px;font-family:'Open Sans',sans-serif;font-size:10px;color:#8ab4d3}
.hire h3{font-family:'Open Sans',sans-serif;font-weight:400;font-size:12px;color:#fff}
.hire p{font-size:9.5px;color:#fff;line-height:12px;margin-top:4px;width:190px}
.foot-search{left:268px;top:1105px;width:206px;height:25px;background:#fff;border-radius:3px;font-size:9px;color:#999;padding:7px 7px}
.foot-submit{left:418px;top:1105px;width:56px;height:25px;border-radius:3px;background:linear-gradient(#c9ee52,var(--lime-dark));font-weight:700;font-size:12px;color:#233;text-align:center;line-height:25px}
.links{list-style:none;font-size:9px;color:#fff;line-height:16.5px}
.bottom-bar{left:0;top:1170px;width:949px;height:30px;background:#1a4f78}
.copyright{left:105px;top:1182px;font-size:8px;color:#c6d8e8}
.foot-social{top:1176px;width:18px;height:18px;border-radius:50%;background:#6f8ea8}
</style>
</head>
<body>

<header class="abs site-header">
  <div class="abs brand">
    <div class="brand-name">Mipsko</div>
    <div class="brand-tag">The new way to give.</div>
  </div>
  <div class="abs social" style="left:530px"><span style="background:#3b5b98"></span><span style="background:#39a6d8"></span><span style="background:#f07b2b"></span></div>
  <div class="abs auth">Login &nbsp;| &nbsp;Register</div>
  <div class="abs search">Search donated talent:</div>
  <div class="abs nav active" style="left:408px;width:53px">Home</div>
  <div class="abs nav" style="left:469px;width:140px">Search Donated Services</div>
  <div class="abs nav" style="left:617px;width:141px">Search Help Wanted Ads</div>
  <div class="abs nav" style="left:766px;width:80px">How It Works</div>
</header>

<section class="abs hero">
</section>
<h1 class="abs hero open" style="background:none;height:auto;width:auto;left:100px;top:145px">New Way To give</h1>
<p class="abs hero-lede">Most people want to make a difference, but getting involved with the cause you care about can be a challenge. That's how Mipsko changes the world of giving!</p>

<div class="abs action" style="left:104px">
  <svg width="50" height="50" viewBox="0 0 50 50"><path d="M8 26h34a17 15 0 0 1-34 0z" fill="#3a3a2a"/><path d="M2 30h46" stroke="#3a3a2a" stroke-width="1.5" stroke-dasharray="2 2"/><circle cx="25" cy="14" r="5" fill="none" stroke="#3a3a2a" stroke-width="2.5"/></svg>
</div>
<div class="abs action" style="left:224px">
  <svg width="44" height="50" viewBox="0 0 44 50"><path d="M15 10h14l-4 6a18 18 0 1 1-6 0z" fill="#3a3a2a"/><text x="22" y="40" text-anchor="middle" font-size="18" font-weight="700" fill="#b6e03a" font-family="Arial">$</text></svg>
</div>
<div class="abs action" style="left:345px">
  <svg width="54" height="54" viewBox="0 0 54 54"><circle cx="27" cy="27" r="25" fill="#3a3a2a"/><circle cx="19" cy="21" r="3.5" fill="#b6e03a"/><circle cx="35" cy="21" r="3.5" fill="#b6e03a"/><path d="M15 31q12 13 24 0" fill="none" stroke="#b6e03a" stroke-width="3.5" stroke-linecap="round"/></svg>
</div>
<div class="abs action-label" style="left:83px">Donate<br>Your Services</div>
<div class="abs action-label" style="left:203px">Buy<br>Donated Services</div>
<div class="abs action-label" style="left:324px">Help The<br>People</div>

<div class="abs community" role="img" aria-label="Circular mosaic of member profile photos"></div>
<div class="abs bubble" style="left:541px;top:333px;width:34px;height:34px" role="img" aria-label="Member photo"></div>
<div class="abs bubble" style="left:515px;top:355px;width:24px;height:24px"></div>
<div class="abs bubble" style="left:490px;top:368px;width:20px;height:20px"></div>
<div class="abs bubble" style="left:471px;top:382px;width:14px;height:14px"></div>
<div class="abs bubble" style="left:460px;top:393px;width:8px;height:8px;border-width:1px"></div>

<main>
  <div class="abs video" role="img" aria-label="60 second overview video still showing a smiling child"></div>
  <div class="abs play"><svg width="32" height="32" viewBox="0 0 32 32"><path d="M12 9l12 7-12 7z" fill="#fff"/></svg></div>
  <div class="abs video-cap">(60 Second Video)</div>
  <div class="abs video-shadow"></div>

  <div class="abs intro-head">JUST LAUNCHED! Mipsko is hot off the press!<br>Welcome to our first visitors.</div>
  <p class="abs intro-text" style="top:490px">Most people want to make a difference, but getting involved with the cause you care about can be a challenge. That's how Mipsko changes the world of giving!</p>
  <p class="abs intro-text" style="top:530px">Everyone has talents - some professional and some hobbies. Lots of people and companies need people with talent. Mipsko enables those with talent to volunteer their time to those who need to hire people with skills -- while benefiting the charity of your choice.</p>
  <div class="abs share" style="left:275px">&#9650; Like</div>
  <div class="abs share" style="left:325px;background:#fff">205</div>
  <div class="abs share" style="left:354px">&#10148; Post</div>
  <div class="abs share" style="left:400px">&#8634; Share</div>
  <div class="abs share" style="left:451px">&#9993; Email</div>

  <aside class="abs charity">
    <div class="box-head">Help any Charity</div>
    <div class="charity-name"><i></i>Cedar Trust</div>
    <div class="dots"><span></span><span></span><span></span><span></span><span></span></div>
  </aside>

  <div class="abs banner">
    <h3>I want to list my talent!</h3>
    <p>Have a talent you would like to donate to help raise money for those in need?</p>
    <div class="cta">Create a FREE Account!</div>
    <div class="banner-mark">Mipsko</div>
  </div>

  <section class="abs panel" style="left:103px">
    <div class="box-head">Volunteer Donated Services</div>
    <div class="view-all">View All</div>
    <div class="item" style="top:42px">
      <div class="photo" role="img" aria-label="Volunteer profile photo" style="background:linear-gradient(#9a8a80,#4a3f3a)"></div>
      <h4>Owen Marsh</h4>
      <div class="meta">Service Provided: Website design</div>
      <div class="desc">I've worked in Information Technology ("computers") for over 20 years. ...</div>
      <div class="more">read more</div><div class="stat">Projects Done (0)</div>
    </div>
    <div class="item" style="top:137px;padding-top:10px">
      <div class="photo" role="img" aria-label="Volunteer profile photo" style="top:10px;background:linear-gradient(#6e5a4e,#3a2e28)"></div>
      <h4 style="top:10px">Leo Haskins</h4>
      <div class="meta" style="top:27px">Service Provided: labor</div>
      <div class="desc" style="top:39px">Currently unemployed and part of the Island Builders Trainee Program, awaiting for job call....</div>
      <div class="more" style="top:80px">read more</div><div class="stat" style="top:83px">Projects Done (0)</div>
    </div>
  </section>

  <section class="abs panel" style="left:499px">
    <div class="box-head">Help Wanted Ads</div>
    <div class="view-all">View All</div>
    <div class="item" style="top:42px">
      <div class="photo" role="img" aria-label="Customer profile photo" style="background:linear-gradient(#3a2c24,#111)"></div>
      <h4>Pet groomer</h4>
      <div class="meta">Location: Norfolk, VA</div>
      <div class="desc">I have 3 dogs I would like to have groomed by a mobile groomer. 2 chihuahuas and 1 dachshund mix. ...</div>
      <div class="more">read more</div><div class="stat">Approximate Budget: $50</div>
    </div>
    <div class="item" style="top:137px">
      <div class="photo" role="img" aria-label="Customer profile photo" style="top:10px;background:linear-gradient(#3a2c24,#111)"></div>
      <h4 style="top:10px">Massage Therapist</h4>
      <div class="meta" style="top:27px">Location: Norfolk, VA</div>
      <div class="desc" style="top:39px">I am interested in getting a monthly massage from a masseuse who would like the funds to help a charity. ....</div>
      <div class="more" style="top:80px">read more</div><div class="stat" style="top:83px">Approximate Budget: $60</div>
    </div>
  </section>
</main>

<footer>
  <div class="abs site-footer"></div>
  <div class="abs foot-brand">Mipsko</div>
  <div class="abs foot-tag">The new way to give.</div>
  <div class="abs hire" style="left:270px;top:1059px">
    <h3>I want to hire donated talent!</h3>
    <p>Looking for an artist, need a music lesson, searching for a handy man?</p>
  </div>
  <div class="abs foot-search">Search donated talent:</div>
  <div class="abs foot-submit">Submit</div>
  <ul class="abs links" style="left:513px;top:1057px"><li>Volunteer Opportunity</li><li>Volunteering Programs</li><li>Local Volunteer Opportunities</li><li>Local Volunteer Work</li><li>Local Volunteering</li></ul>
  <ul class="abs links" style="left:671px;top:1057px"><li>Home</li><li>Newsroom</li><li>About Mipsko</li><li>Charities</li><li>FAQ</li></ul>
  <ul class="abs links" style="left:765px;top:1057px"><li>Contact Mipsko</li><li>Terms &amp; Conditions</li><li>Privacy Policy</li><li>Blog</li><li>Site Map</li></ul>
  <div class="abs bottom-bar"></div>
  <div class="abs copyright">Copyright © 2012 Mipsko, Inc. All rights reserved.Mipsko® is a registered trademark of Mipsko, Inc. Patent Pending.</div>
  <div class="abs foot-social" style="left:778px"></div>
  <div class="abs foot-social" style="left:802px"></div>
  <div class="abs foot-social" style="left:826px"></div>
</footer>

</body>
</html>
```